Flyer Design

A flyer to introduce our new business called Smilewagons on Wheels ,we are a mobile dental hygienist service based in the Teesside area of England.We use portable equipment to treat clients where they live or work Since may 2013 in the uk hygienists no longer need to work with a dentist ,therefore clients can now access dental hygiene care without seeing a dentist.We offer scale and polish ,oral hygiene advice .Our colours are pink,green and purple.we would like to stress the importance of a regular professional clean with the convenience of being treated at home

Target Market(s)

over 18 years of age who choose or need to have there scale and polish at home

Industry/Entity Type

Dental

Colors
e34297
9ccb3b
876aae

Requirements
Must have
• ,must have our logo and our contact details tel 07812460395 and email info@smilewagonsonwheels.co.uk
The hygienists names Moira Palfrey and Janet Ruddock
eye catching and colourful ,not to many words,but getting across we are for anyone who chooses or needs their treatment at home
Nice to have
• we would like the logo to be prominent ,our colours are pink ,green and purple .the font easy to read for older people
Should not have
• A lot of writing on the front the page ,

```html
<!DOCTYPE html>
<html lang="en">
<head>
<meta charset="utf-8">
<title>Smilewagons on Wheels – Mobile Dental Hygienists</title>
<link rel="stylesheet" href="https://fonts.googleapis.com/css2?family=Open+Sans:wght@400;600&display=swap">
<style>
  :root {
    --green: #7bbb6a;
    --pink: #cf78aa;
    --brand-pink: #d45a9a;
    --brand-green: #6cb84a;
    --art-dark: #111111;
    --art-mid: #2a2a2a;
    --screen: #f3f1f2;
    --ink: #111111;
  }
  html, body { margin: 0; padding: 0; overflow: hidden; }
  .flyer {
    position: relative;
    width: 932px;
    height: 1200px;
    overflow: hidden;
    background: linear-gradient(to bottom, var(--green) 0 950px, var(--pink) 950px 100%);
    font-family: "Open Sans", sans-serif;
  }
  .phone-illustration {
    position: absolute;
    left: 45px; top: 90px;
    width: 835px; height: 1020px;
    border-radius: 48px;
    background: linear-gradient(160deg, var(--art-mid), var(--art-dark) 60%);
  }
  .screen {
    position: absolute;
    left: 230px; top: 252px;
    width: 470px; height: 698px;
    background: var(--screen);
    text-align: center;
    color: var(--ink);
  }
  .brand {
    position: absolute;
    left: 0; right: 0; top: 47px;
    display: flex;
    align-items: center;
    justify-content: center;
    gap: 8px;
    height: 26px;
  }
  .brand-name {
    font-size: 20px;
    font-weight: 600;
    color: var(--brand-pink);
  }
  .brand-dot {
    width: 14px; height: 14px;
    border-radius: 50%;
    background: var(--brand-green);
  }
  .tagline {
    position: absolute;
    left: 0; right: 0; top: 131px;
    margin: 0;
    font-size: 14px;
    font-weight: 600;
    color: var(--brand-green);
  }
  .intro {
    position: absolute;
    left: 45px; top: 198px;
    width: 380px;
    margin: 0;
    font-size: 16.5px;
    line-height: 25.2px;
  }
  .contact {
    position: absolute;
    left: 0; right: 0; top: 603px;
    margin: 0;
    font-size: 16.5px;
    line-height: 25.2px;
  }
  .contact span { display: block; }
</style>
</head>
<body>
<main class="flyer">
  <div class="phone-illustration" role="img" aria-label="Illustration of a black smartphone held upright by two cartoon toothbrushes with arms, brush heads at top left and bottom right"></div>

  <section class="screen">
    <div class="brand">
      <span class="brand-dot"></span>
      <span class="brand-name">Smilewagons on Wheels</span>
    </div>
    <p class="tagline">Mobile Dental Hygienists</p>

    <p class="intro">Smilewagons on Wheels is a mobile dental hygienist service based in Teesside. We use portable equipment to treat you either in your place of residence or work place. Since May 2013, the UK hygienists no longer need to work with a dentist, meaning you can now access dental hygiene care without seeing a dentist. Our mobile service offers scale and polish as well as oral hygiene advice. We would like to stress the importance of a regular professional clean with the convenience of being treated in a comfortable and familiar environment.</p>

    <p class="contact">
      <span class="contact-phone">07812460395</span>
      <span class="contact-email">info@smilewagonsonwheels.co.uk</span>
      <span class="contact-team">Hygienists: Moira Palfrey and Janet Ruddock</span>
    </p>
  </section>
</main>
</body>
</html>
```